Leuchtkasten für Pflegedienst
Zielgruppe
Wir sind ein ambulnter Pflegedienst in Rostock. Derzeit befindet sich am Haus ein runder Leuchtkasten mit dem alten Logo. Das Logo wurde erneuert. Nun soll der Leuchtkasten mit einem Durchmessr von 80 cm neu gestaltet werden.
Aufgabenstellung
bitte zwei unterscheideliche Entwürfe für die Vorder und die Rückseite. Es sollte auf der einen Seite vielleicht das Logo anthalten sein und auf der anderen Seite eine andere kreative Idee. Hauskrankenpflege Sorgenhaus Linde sollten enthalten sein, sowie die Telefonummer 0381-52946138
Auf der anderen Seite wurde ein Schriftzug in Edelstahl rostoptik montiert.
Wichtig ist, dass das der ENtwurf auf einer durchleichtbaren Folie gedruckt werden kann.
Der KAffee slogan war füe eine andere Aktion und sollte nicht auf den Leuchtkasten.

```html
<!DOCTYPE html>
<html lang="de">
<head>
<meta charset="utf-8">
<title>Leuchtkasten Sorgenhaus Linde – Vorder- und Rückseite</title>
<link rel="stylesheet" href="https://fonts.googleapis.com/css2?family=Kaushan+Script&family=Open+Sans:wght@700;800&display=swap">
<style>
  :root {
    --navy: #2c3a5f;
    --teal: #72cbbd;
    --teal-light: #8fd8cc;
    --sky: #3b8fd3;
    --white: #ffffff;
    --page: #ecebe8;
    --photo-top: #f3dcdc;
    --photo-bottom: #f7eef0;
  }
  html, body {
    margin: 0;
    padding: 0;
    overflow: hidden;
  }
  body {
    width: 857px;
    height: 1200px;
    background: var(--page);
    display: flex;
    flex-direction: column;
    align-items: center;
    justify-content: space-evenly;
  }
  .sign-face {
    width: 540px;
    height: 540px;
    display: block;
  }
  .script {
    font-family: "Kaushan Script", cursive;
  }
  .sans {
    font-family: "Open Sans", sans-serif;
    font-weight: 800;
  }
</style>
</head>
<body>

<!-- Vorderseite: Name und Telefon -->
<svg class="sign-face sign-front" viewBox="0 0 500 500" aria-label="Vorderseite Leuchtkasten">
  <defs>
    <clipPath id="front-disc"><circle cx="250" cy="250" r="250"/></clipPath>
    <path id="front-arc" d="M70,240 A182,182 0 0 1 430,240"/>
  </defs>
  <g clip-path="url(#front-disc)">
    <rect width="500" height="500" fill="var(--navy)"/>
    <path class="wave-left" d="M0,285 C60,272 110,292 130,340 C150,400 120,460 100,500 L0,500 Z" fill="var(--teal)"/>
    <path class="wave-bottom" d="M0,425 C150,440 250,450 330,400 C380,370 430,360 500,370 L500,500 L0,500 Z" fill="var(--teal)"/>
  </g>

  <text class="script headline" font-size="40" fill="var(--white)">
    <textPath href="#front-arc" startOffset="50%" text-anchor="middle">Hauskrankenpflege</textPath>
  </text>

  <g class="brand-mark">
    <circle cx="250" cy="160" r="42" fill="none" stroke="var(--white)" stroke-width="6"/>
    <text class="script" x="250" y="236" font-size="24" fill="var(--white)" text-anchor="middle">Sorgenhaus Linde</text>
  </g>

  <text class="script name-main" x="255" y="305" font-size="42" fill="var(--white)" text-anchor="middle">Sorgenhaus</text>
  <text class="script name-accent" x="265" y="352" font-size="48" fill="var(--sky)" text-anchor="middle">Linde</text>

  <g class="phone">
    <circle cx="110" cy="452" r="15" fill="none" stroke="var(--white)" stroke-width="2.5"/>
    <path d="M104,444 q-3,8 4,15 q7,7 14,3 l-2,-4 q-4,2 -8,-2 q-4,-4 -2,-8 z" fill="var(--white)"/>
    <text class="sans" x="138" y="464" font-size="30" fill="var(--white)">0381-52946138</text>
  </g>
</svg>

<!-- Rückseite: Bildmotiv -->
<svg class="sign-face sign-back" viewBox="0 0 500 500" aria-label="Rückseite Leuchtkasten">
  <defs>
    <clipPath id="back-disc"><circle cx="250" cy="250" r="250"/></clipPath>
    <path id="back-arc" d="M70,240 A182,182 0 0 1 430,240"/>
    <linearGradient id="back-sky" x1="0" y1="0" x2="0" y2="1">
      <stop offset="0" stop-color="var(--teal-light)"/>
      <stop offset="1" stop-color="var(--teal)"/>
    </linearGradient>
    <linearGradient id="photo-tone" x1="0" y1="0" x2="0" y2="1">
      <stop offset="0" stop-color="var(--photo-top)"/>
      <stop offset="1" stop-color="var(--photo-bottom)"/>
    </linearGradient>
  </defs>
  <g clip-path="url(#back-disc)">
    <rect width="500" height="500" fill="url(#back-sky)"/>
    <rect class="photo-area" role="img" aria-label="Foto eines fröhlichen älteren Herrn mit Brille, Fliege und Hosenträgern, der ein OK-Zeichen zeigt" x="120" y="125" width="270" height="320" rx="120" fill="url(#photo-tone)"/>
    <path class="wave-bottom" d="M0,318 C70,300 110,335 130,400 L375,400 C395,340 440,318 500,328 L500,500 L0,500 Z" fill="var(--navy)"/>
  </g>

  <text class="script headline" font-size="40" fill="var(--navy)">
    <textPath href="#back-arc" startOffset="50%" text-anchor="middle">Hauskrankenpflege</textPath>
  </text>

  <text x="250" y="452" text-anchor="middle">
    <tspan class="sans" font-size="32" fill="var(--white)">Sorgenhaus </tspan><tspan class="script" font-size="36" fill="var(--sky)">Linde</tspan>
  </text>
</svg>

</body>
</html>
```